Fantasy-Roman sucht eBook-Cover
Bin sehr glücklich mit dem Ergebnis! Alle Erwartungen wurden erfüllt und alle Anregungen oder Veränderungswünsche wurden professionell umgesetzt. Ich kann die Zusammenarbeit mit der Designerin nur empfehlen und werde diese auch in Zukunft anstreben.
Zielgruppe
Autorin; Zielgruppe: Jugendliche, die sich für Mystik und Fantasy interessieren; Covergestaltung eBook
Aufgabenstellung
Es handelt sich um ein Jugendbuch im Genre Fantasy. Dunkelroter Hintergrund, das Symbol sollte deutlich sichtbar sein und ein verspielt verschnörkelter Rahmen wäre schön. Mystisch

```html
<!DOCTYPE html>
<html lang="de">
<head>
<meta charset="utf-8">
<title>Buch Titel – eBook-Cover</title>
<link rel="stylesheet" href="https://fonts.googleapis.com/css2?family=Cinzel:wght@400;500&display=swap">
<style>
  :root {
    --page: #ffffff;
    --leather: #8c141b;
    --leather-dark: #6e0e14;
    --leather-light: #9a1a20;
    --copper: #c27a5f;
    --copper-mid: #b1664d;
    --copper-dark: #9a4a35;
    --emblem: #6c0e15;
    --emblem-edge: #5a0b11;
    --type: #ffffff;
  }
  html, body {
    margin: 0;
    padding: 0;
    width: 848px;
    height: 1200px;
    overflow: hidden;
    background: var(--page);
  }
  .canvas {
    position: relative;
    width: 848px;
    height: 1200px;
    background: var(--page);
  }
  .cover {
    position: absolute;
    left: 184px;
    top: 244px;
    width: 475px;
    height: 736px;
    background: radial-gradient(ellipse at 45% 40%, var(--leather-light) 0%, var(--leather) 55%, var(--leather-dark) 100%);
    overflow: hidden;
  }
  .frame-line {
    position: absolute;
    background: var(--copper-mid);
  }
  .frame-line.top { left: 80px; right: 80px; top: 28px; height: 9px; background: linear-gradient(90deg, var(--copper-dark), var(--copper), var(--copper-dark)); }
  .frame-line.bottom { left: 80px; right: 80px; bottom: 27px; height: 9px; background: linear-gradient(90deg, var(--copper-dark), var(--copper), var(--copper-dark)); }
  .frame-line.left { top: 100px; bottom: 100px; left: 21px; width: 9px; background: linear-gradient(180deg, var(--copper-dark), var(--copper), var(--copper-dark)); }
  .frame-line.right { top: 100px; bottom: 100px; right: 21px; width: 9px; background: linear-gradient(180deg, var(--copper-dark), var(--copper), var(--copper-dark)); }
  .corner-ornament {
    position: absolute;
    width: 70px;
    height: 84px;
    background: linear-gradient(135deg, var(--copper) 0%, var(--copper-dark) 100%);
    border-radius: 6px;
  }
  .corner-ornament.top-left { left: 17px; top: 26px; }
  .corner-ornament.top-right { right: 17px; top: 26px; }
  .corner-ornament.bottom-left { left: 17px; bottom: 20px; }
  .corner-ornament.bottom-right { right: 17px; bottom: 20px; }
  .title {
    margin: 0;
    font-family: "Cinzel", serif;
    font-weight: 400;
    color: var(--type);
    line-height: 1;
  }
  .title span {
    position: absolute;
    font-size: 80px;
    white-space: nowrap;
  }
  .title .line-one { left: 82px; top: 119px; }
  .title .line-two { left: 155px; top: 194px; }
  .emblem {
    position: absolute;
    left: 108px;
    top: 322px;
    width: 263px;
    height: 218px;
    background: var(--emblem);
    border: 2px solid var(--emblem-edge);
    border-radius: 46% 46% 30% 30%;
    box-sizing: border-box;
  }
  .author {
    position: absolute;
    left: 0;
    right: 0;
    top: 630px;
    margin: 0;
    text-align: center;
    font-family: "Cinzel", serif;
    font-size: 27px;
    font-weight: 400;
    color: var(--type);
    letter-spacing: 0.5px;
  }
</style>
</head>
<body>
<div class="canvas">
  <div class="cover">
    <div class="frame-line top"></div>
    <div class="frame-line bottom"></div>
    <div class="frame-line left"></div>
    <div class="frame-line right"></div>

    <div class="corner-ornament top-left" role="img" aria-label="Keltischer Knoten als Rahmenecke"></div>
    <div class="corner-ornament top-right" role="img" aria-label="Keltischer Knoten als Rahmenecke"></div>
    <div class="corner-ornament bottom-left" role="img" aria-label="Keltischer Knoten als Rahmenecke"></div>
    <div class="corner-ornament bottom-right" role="img" aria-label="Keltischer Knoten als Rahmenecke"></div>

    <h1 class="title">
      <span class="line-one">BUCH</span>
      <span class="line-two">TITEL</span>
    </h1>

    <div class="emblem" role="img" aria-label="Eingeprägtes Symbol: Schleife über einem verschnörkelten Kreuz"></div>

    <p class="author">Author Name</p>
  </div>
</div>
</body>
</html>
```